Business card for a doctor's practice

Would like a business card for a Pulmonary ( lung) doctor. I would like to include a logo with something in reference to air or oxygen or lungs. Would like the color red included somehow. Name of the company is Breathwell Medical Associates of Eastern Ridgeford and we specialize in Pulmonary Medicine,. I would like something streamlined and modern
Target Market(s)
Patients, hospitals, other doctors
Industry/Entity Type
Business
Contact Information for Business Card
Would like business details superimposed on a logo somehow

```html
<!DOCTYPE html>
<html lang="en">
<head>
<meta charset="utf-8">
<title>Breathwell Medical Associates – Business Card</title>
<link rel="stylesheet" href="https://fonts.googleapis.com/css2?family=Roboto+Condensed:ital,wght@0,700;1,700&display=swap">
<style>
  :root {
    --paper: #ffffff;
    --brand-red: #e62128;
    --band-shadow: #2e2e2e;
    --grey-dark: #a6a6a6;
    --grey-light: #e6e6e6;
    --ink-light: #ffffff;
    --text-shadow: rgba(0, 0, 0, 0.85);
  }
  html, body {
    margin: 0;
    padding: 0;
    width: 1200px;
    height: 652px;
    overflow: hidden;
    background: var(--paper);
  }
  .card {
    position: relative;
    width: 1200px;
    height: 652px;
    background: var(--paper);
    overflow: hidden;
    font-family: "Roboto Condensed", "Arial Narrow", sans-serif;
  }
  .card-shapes {
    position: absolute;
    inset: 0;
  }
  .brand {
    position: absolute;
    left: 20px;
    top: 215px;
    width: 470px;
    display: flex;
    align-items: center;
    gap: 18px;
    transform: rotate(-36deg);
    transform-origin: center;
    color: var(--brand-red);
    font-weight: 700;
    font-style: normal;
    font-size: 32px;
    line-height: 1.1;
    letter-spacing: 1px;
    text-transform: uppercase;
  }
  .brand-mark {
    flex: 0 0 auto;
    width: 46px;
    height: 46px;
    background: var(--brand-red);
  }
  .brand-name {
    margin: 0;
    font: inherit;
  }
  .identity {
    position: absolute;
    right: 53px;
    top: 176px;
    text-align: right;
    color: var(--ink-light);
    font-style: italic;
    font-weight: 700;
    text-shadow: 3px 3px 3px var(--text-shadow);
  }
  .identity-name {
    margin: 0;
    font-size: 56px;
    line-height: 1;
    letter-spacing: 1px;
  }
  .identity-role {
    margin: 6px 0 0;
    font-size: 30px;
    line-height: 1.1;
  }
  .contact {
    position: absolute;
    right: 53px;
    top: 375px;
    margin: 0;
    padding: 0;
    list-style: none;
    text-align: right;
    color: var(--ink-light);
    font-style: italic;
    font-weight: 700;
    font-size: 28px;
    line-height: 40.5px;
    text-shadow: 2px 2px 2px var(--text-shadow);
  }
</style>
</head>
<body>
  <div class="card">
    <svg class="card-shapes" width="1200" height="652" viewBox="0 0 1200 652" aria-hidden="true">
      <defs>
        <linearGradient id="grey-field" x1="1" y1="0" x2="0.3" y2="1">
          <stop offset="0" stop-color="var(--grey-dark)" style="stop-color: var(--grey-dark)"/>
          <stop offset="1" stop-color="var(--grey-light)" style="stop-color: var(--grey-light)"/>
        </linearGradient>
      </defs>
      <polygon class="grey-field" points="820,0 1200,0 1200,652 0,652 0,606" fill="url(#grey-field)"/>
      <polygon class="band-shadow" points="405,304 640,304 640,312 418,316" style="fill: var(--band-shadow)"/>
      <polygon class="name-band" points="607,153 1200,153 1200,304 405,304" style="fill: var(--brand-red)"/>
    </svg>

    <div class="brand">
      <span class="brand-mark"></span>
      <p class="brand-name">Breathwell Medical Associates of Eastern Ridgeford</p>
    </div>

    <div class="identity">
      <h1 class="identity-name">DANIEL R. HAYES</h1>
      <p class="identity-role">General Manager</p>
    </div>

    <ul class="contact">
      <li class="contact-street">Linden Road, Harbor Street,</li>
      <li class="contact-city">48210, Ridgeford</li>
      <li class="contact-phone">555 30 10 - 555 30 11</li>
      <li class="contact-email">info@breathwellmed.com</li>
      <li class="contact-web">www.breathwellmed.com</li>
    </ul>
  </div>
</body>
</html>
```